Varemo Group Business Card Design

The CEO is looking for a new trendy look for his business card.
You can stay with current branding or come up with something new/creative. It can be 3D, including Medical Office buildings. You can use our logo in a variety of colors. Please include name, title, company name, company website, email address, cell number

Target Market(s)

Real Estate Development and Construction

Industry/Entity Type

Health care real estate

Contact Information for Business Card

Rohesh Kumbar, CEO M-727.418.9062 E-roheshkumbar@varemo.com Address:4100 Lindell Ave, Tampa, FL 33611 www.varemo.com

Font styles to use
Other font styles liked:
• Be creative

Requirements
Must have
• Creative, trendy look
Nice to have
• Please go to our website to get a feel- www. varemo.com
Should not have
• small fonts

```html
<!DOCTYPE html>
<html lang="en">
<head>
<meta charset="utf-8">
<title>Varemo Group Business Card</title>
<link rel="stylesheet" href="https://fonts.googleapis.com/css2?family=Arimo:wght@400;700&display=swap">
<style>
  :root {
    --backdrop: #e9e9e7;
    --card: #2a2a2c;
    --card-edge: #b01c27;
    --brand-red: #b01c27;
    --accent-navy: #1f2f5c;
    --ink-light: #eeeeee;
    --ghost: #353537;
  }
  * { margin: 0; padding: 0; box-sizing: border-box; }
  html, body { width: 1200px; height: 801px; overflow: hidden; }
  body {
    background: var(--backdrop);
    font-family: "Arimo", Arial, sans-serif;
    position: relative;
  }
  .card {
    position: absolute;
    top: 252px;
    width: 520px;
    height: 297px;
    background: var(--card);
    border-bottom: 3px solid var(--card-edge);
    overflow: hidden;
    box-shadow: 0 10px 24px rgba(0,0,0,.18);
  }
  .card--front { left: 50px; }
  .card--back { left: 630px; }

  .corner-band { position: absolute; left: 0; top: 0; width: 520px; height: 297px; }

  .front-wordmark {
    position: absolute;
    left: 34px;
    top: 96px;
    color: var(--brand-red);
    font-weight: 700;
    font-size: 32px;
    letter-spacing: -1px;
    line-height: 1;
    white-space: nowrap;
  }

  .contact {
    position: absolute;
    left: 290px;
    top: 42px;
    color: var(--ink-light);
    font-size: 15px;
    line-height: 1.32;
  }
  .contact__name {
    color: var(--brand-red);
    font-size: 19px;
    font-weight: 700;
    text-transform: uppercase;
    margin-bottom: 2px;
  }
  .contact__title { margin-bottom: 10px; }
  .contact__address { margin-bottom: 10px; }
  .contact__line { display: flex; align-items: center; gap: 7px; }
  .contact__icon { width: 14px; height: 14px; flex: none; }

  .ghost-name {
    position: absolute;
    left: -10px;
    top: 150px;
    color: var(--ghost);
    font-weight: 700;
    font-size: 168px;
    letter-spacing: -8px;
    line-height: 1;
    white-space: nowrap;
  }
  .back-wordmark {
    position: absolute;
    left: 80px;
    top: 72px;
    color: var(--brand-red);
    font-weight: 700;
    font-size: 56px;
    letter-spacing: -2px;
    line-height: 1;
    white-space: nowrap;
  }
</style>
</head>
<body>

  <section class="card card--front" aria-label="Business card front">
    <svg class="corner-band" viewBox="0 0 520 297" aria-hidden="true">
      <path d="M0 160 C 90 160, 170 215, 200 297 L 0 297 Z" fill="var(--brand-red)"/>
      <path d="M0 150 C 100 150, 185 210, 214 297" fill="none" stroke="var(--accent-navy)" stroke-width="5"/>
    </svg>
    <div class="front-wordmark">Varemo Group</div>

    <div class="contact">
      <div class="contact__name">Rohesh Kumbar</div>
      <div class="contact__title">CEO</div>
      <div class="contact__address">4100 Lindell Ave<br>Tampa, FL 33611</div>
      <div class="contact__line">
        <svg class="contact__icon" viewBox="0 0 14 14" aria-hidden="true"><circle cx="7" cy="7" r="7" fill="var(--brand-red)"/><path d="M4 4.2c.6-.6 1.2-.5 1.5 0l.6 1c.2.4 0 .7-.3 1 .4.9 1 1.5 1.9 1.9.3-.3.6-.5 1-.3l1 .6c.5.3.6.9 0 1.5-1.7 1.7-7.4-4-5.7-5.7z" fill="var(--card)"/></svg>
        <span>727.418.9062</span>
      </div>
      <div class="contact__line">
        <svg class="contact__icon" viewBox="0 0 14 14" aria-hidden="true"><circle cx="7" cy="7" r="7" fill="var(--brand-red)"/><rect x="3.5" y="4.5" width="7" height="5" fill="var(--card)"/><path d="M3.5 4.5 7 7.3 10.5 4.5" fill="none" stroke="var(--brand-red)" stroke-width=".9"/></svg>
        <span>roheshkumbar@varemo.com</span>
      </div>
      <div class="contact__line">
        <svg class="contact__icon" viewBox="0 0 14 14" aria-hidden="true"><circle cx="7" cy="7" r="7" fill="var(--brand-red)"/><circle cx="7" cy="7" r="3.6" fill="none" stroke="var(--card)" stroke-width="1"/><path d="M3.4 7h7.2M7 3.4c-1.6 2-1.6 5.2 0 7.2M7 3.4c1.6 2 1.6 5.2 0 7.2" fill="none" stroke="var(--card)" stroke-width=".8"/></svg>
        <span>www.varemo.com</span>
      </div>
    </div>
  </section>

  <section class="card card--back" aria-label="Business card back">
    <div class="ghost-name">Varemo</div>
    <div class="back-wordmark">Varemo Group</div>
  </section>

</body>
</html>
```